Ferncrest Dental, LLC business card project

Business card to be designed with current logo.
Dental office- please keep design of card that looks clean and professional.
Please include the following info:
Ferncrest Dental, LLC
Dr. Lorna Pettigrew
2871 Marlowe Street
Bethlehem, PA 18093
610-555-0193
ferncrestdental.office@examplemail.test
Hello everyone-
Reason: Just got back from overseas- will look at all designs and provide feedback. Thank you!
Reason: Polling my friends for the final selection-
thank you to all those that participated- so many talented designers!

```html
<!DOCTYPE html>
<html lang="en">
<head>
<meta charset="utf-8">
<title>Ferncrest Dental, LLC — Business Card</title>
<link rel="stylesheet" href="https://fonts.googleapis.com/css2?family=Questrial&family=Libre+Baskerville:wght@700&family=PT+Sans&display=swap">
<style>
  :root {
    --stage-bg: #e6e9ec;
    --card-white: #ffffff;
    --band-green: #b4d334;
    --band-edge: #2f3b1d;
    --brand-green: #6a9e3e;
    --name-green: #6b9a4b;
    --ink: #1f2418;
    --tooth-light: #ffffff;
    --tooth-shade: #d5d8da;
    --pedestal-shade: #e3e5e6;
  }
  * { margin: 0; padding: 0; box-sizing: border-box; }
  html, body {
    width: 1200px;
    height: 1000px;
    overflow: hidden;
    background: var(--stage-bg);
  }
  .card {
    position: absolute;
    left: 100px;
    top: 215px;
    width: 1000px;
    height: 569px;
    background: var(--card-white);
    overflow: hidden;
    box-shadow: 0 6px 24px rgba(0,0,0,0.15);
  }
  .contact-band {
    position: absolute;
    left: 0;
    top: 377px;
    width: 100%;
    height: 192px;
    background: var(--band-green);
    border-top: 4px solid var(--band-edge);
  }
  .tooth-art {
    position: absolute;
    left: 600px;
    top: 60px;
    width: 380px;
    height: 400px;
  }
  .brand {
    position: absolute;
    left: 96px;
    top: 118px;
    display: flex;
    align-items: center;
    gap: 24px;
  }
  .brand-dot {
    width: 58px;
    height: 58px;
    border-radius: 50%;
    background: var(--brand-green);
  }
  .brand-name {
    font-family: "Questrial", sans-serif;
    font-size: 74px;
    line-height: 1;
    color: var(--brand-green);
    white-space: nowrap;
  }
  .dentist-name {
    position: absolute;
    left: 560px;
    top: 252px;
    font-family: "Libre Baskerville", serif;
    font-weight: 700;
    font-size: 33px;
    letter-spacing: 0.5px;
    color: var(--name-green);
    white-space: nowrap;
  }
  .contact-list {
    position: absolute;
    left: 28px;
    top: 398px;
    display: grid;
    grid-template-columns: 138px auto;
    column-gap: 10px;
    row-gap: 4px;
    font-family: "PT Sans", sans-serif;
    font-size: 25px;
    line-height: 30px;
    color: var(--ink);
  }
  .contact-label { text-align: right; }
</style>
</head>
<body>
  <div class="card">
    <div class="contact-band"></div>

    <svg class="tooth-art" viewBox="0 0 380 400" role="img" aria-label="Glossy white tooth illustration standing on a white oval pedestal">
      <defs>
        <radialGradient id="pedestal-fill" cx="50%" cy="40%" r="60%">
          <stop offset="0%" stop-color="var(--pedestal-shade)"/>
          <stop offset="100%" stop-color="#ffffff"/>
        </radialGradient>
        <linearGradient id="tooth-fill" x1="0" y1="0" x2="1" y2="1">
          <stop offset="0%" stop-color="var(--tooth-light)"/>
          <stop offset="100%" stop-color="var(--tooth-shade)"/>
        </linearGradient>
      </defs>
      <ellipse cx="192" cy="343" rx="172" ry="52" fill="url(#pedestal-fill)"/>
      <rect x="70" y="10" width="230" height="370" rx="70" fill="url(#tooth-fill)"/>
    </svg>

    <div class="brand">
      <span class="brand-dot"></span>
      <span class="brand-name">Ferncrest Dental</span>
    </div>

    <p class="dentist-name">Dr. Lorna Pettigrew</p>

    <div class="contact-list">
      <span class="contact-label">Address:</span><span>2871 Marlowe Street</span>
      <span></span><span>Bethlehem, PA 18093</span>
      <span class="contact-label">Tel:</span><span>610-555-0193</span>
      <span class="contact-label">E-Mail:</span><span>ferncrestdental.office@examplemail.test</span>
    </div>
  </div>
</body>
</html>
```